Advertisement for linkora Ad

We are looking to copy a mailer style design that would normally be sent out to a mailbox. However we have decided to simply use it and run an add on Linkora. please check photo sizes for linkora to make sure your design will work.

also please try to use the colors from our website: brightmeadowclub@postvane.net

we want the same layout as the ad we sent in the files, with different photos and color scheme.

Target Market(s)

dog owners with busy schedules

Font styles to use
Sans Serif

Colors

Designer to choose only greyscale colors for use in the design.

```html
<!DOCTYPE html>
<html lang="en">
<head>
<meta charset="utf-8">
<title>Bright Meadow Canine Club – Dog Daycare Ad</title>
<link rel="stylesheet" href="https://fonts.googleapis.com/css2?family=Arimo:wght@400;700&family=Source+Sans+3:wght@400&display=swap">
<style>
  :root {
    --panel-grey: #7d7d7d;
    --accent-grey: #d2d2d2;
    --charcoal: #393939;
    --white: #ffffff;
    --ink: #1d1d1d;
    --photo-light: #ebebeb;
    --photo-mid: #c9c9c9;
    --photo-dark: #8c8c8c;
  }
  * { margin: 0; padding: 0; box-sizing: border-box; }
  html, body { width: 1200px; height: 662px; overflow: hidden; background: var(--white); }
  .ad { position: relative; width: 1200px; height: 662px; overflow: hidden; font-family: "Arimo", Arial, sans-serif; }

  .hero { position: absolute; left: 0; top: 0; width: 1200px; height: 418px; }
  .hero-photo {
    position: absolute; left: 0; top: 0; width: 700px; height: 418px;
    background: linear-gradient(120deg, var(--photo-light) 0%, var(--photo-mid) 45%, var(--photo-dark) 75%, var(--photo-light) 100%);
  }
  .hero-panel { position: absolute; left: 0; top: 0; }

  .brand-box {
    position: absolute; left: 29px; top: 307px; width: 169px; height: 89px;
    background: var(--white); display: flex; align-items: center; justify-content: center; gap: 7px;
    padding: 0 8px;
  }
  .brand-box .dot { width: 12px; height: 12px; border-radius: 50%; background: var(--ink); flex: none; }
  .brand-box .name { font-family: "Arimo", Arial, sans-serif; font-weight: 700; font-size: 15px; line-height: 1.15; color: var(--ink); }

  .headline {
    position: absolute; left: 705px; top: 42px; color: var(--white);
    font-weight: 700; font-size: 42px; line-height: 41px;
  }
  .perks {
    position: absolute; left: 704px; top: 139px; color: var(--white);
    font-size: 22px; line-height: 29px; list-style: none;
  }
  .perks .note { font-size: 16px; line-height: 24px; margin-top: 4px; }

  .contact-box {
    position: absolute; left: 708px; top: 277px; width: 462px; height: 114px;
    background: var(--white); padding: 15px 20px 0;
    font-family: "Source Sans 3", "Myriad Pro", sans-serif; font-size: 24px; line-height: 33px; color: var(--ink);
    font-style: normal;
  }

  .offers { position: absolute; left: 0; top: 418px; width: 1200px; height: 244px; background: var(--charcoal); }
  .offer { position: absolute; top: 51px; text-align: center; }
  .offer-1 { left: 0; width: 403px; }
  .offer-2 { left: 403px; width: 398px; }
  .offer-3 { left: 801px; width: 399px; }
  .offer-title { color: var(--accent-grey); font-weight: 700; font-size: 39px; line-height: 38px; letter-spacing: -0.3px; }
  .offer-terms {
    margin-top: 13px; color: var(--white);
    font-family: "Source Sans 3", "Myriad Pro", sans-serif; font-size: 24.5px; line-height: 25px;
  }
  .divider { position: absolute; top: 57px; width: 0; height: 187px; border-left: 2px dashed var(--white); }
  .divider-1 { left: 403px; }
  .divider-2 { left: 800px; }

  .expiry {
    position: absolute; left: 498px; top: 210px; width: 205px; height: 34px;
    background: var(--white); color: var(--ink); text-align: center;
    font-family: "Source Sans 3", "Myriad Pro", sans-serif; font-size: 28px; line-height: 38px;
  }
</style>
</head>
<body>
<main class="ad">
  <section class="hero">
    <div class="hero-photo" role="img" aria-label="Woman sitting on the floor of a bright room, smiling at a black and white husky"></div>
    <svg class="hero-panel" width="1200" height="418" viewBox="0 0 1200 418" aria-hidden="true">
      <polygon points="601,0 1200,0 1200,418 683,418" fill="var(--panel-grey)"/>
    </svg>

    <div class="brand-box">
      <span class="dot"></span>
      <span class="name">Bright Meadow Canine Club</span>
    </div>

    <h1 class="headline">NOT YOUR TYPICAL<br>DOG DAYCARE</h1>
    <ul class="perks">
      <li>SAFE, OPEN-PLAY DAYCARE</li>
      <li>EXCERCISE &amp; EDUCATION</li>
      <li>FUN FILLED DAYS WITH THEIR BFFF</li>
      <li class="note">(BEST FURRY FRIEND FOREVER)</li>
    </ul>

    <address class="contact-box">
      Bright Meadow Canine Club<br>
      845 west Orchard Avenue Maple Ridge IA<br>
      555-204-7193
    </address>
  </section>

  <section class="offers">
    <div class="offer offer-1">
      <h2 class="offer-title">FREE FIRST DAY<br>OF DAY CARE!*</h2>
      <p class="offer-terms">Advanced reservationns required<br>call to schedule your appoinnment.</p>
    </div>
    <div class="divider divider-1"></div>
    <div class="offer offer-2">
      <h2 class="offer-title">ONE FREE<br>BATH!*</h2>
      <p class="offer-terms">Advanced reservationns required<br>call to schedule your appoinnment.</p>
    </div>
    <div class="divider divider-2"></div>
    <div class="offer offer-3">
      <h2 class="offer-title">$20 OFF<br>FIRST GROOM</h2>
      <p class="offer-terms">Advanced reservationns required<br>call to schedule your appoinnment.</p>
    </div>
    <div class="expiry">use by 8/31/20</div>
  </section>
</main>
</body>
</html>
```